Snake breeder. Cedar hollow scales

I would like it to have the same vibe as my logo will attach pictures
Target Market(s)
Snake enthusiasts
Requirements
Must have
- Must have mine and my wife’s names, Grant and Melinda Barlow. Email cedarhollowscales@mailhub.example. And Instagram insignia with or with our name cedarhollowscales. Our location Briar Bend, TX. And also reptile breeder.

Should not have
- Cartoonish vibe

```html
<!DOCTYPE html>
<html lang="en">
<head>
<meta charset="utf-8">
<title>Cedar Hollow Scales – Business Cards</title>
<link rel="stylesheet" href="https://fonts.googleapis.com/css2?family=Cinzel:wght@400;600&family=Roboto:wght@400;500&display=swap">
<style>
  :root {
    --backdrop: #3a3a3a;
    --card: #1f1c1c;
    --card-edge: #2a2626;
    --gold: #f5c518;
    --white: #ffffff;
    --forest: rgba(58,52,36,.85);
  }
  * { margin: 0; padding: 0; box-sizing: border-box; }
  html, body {
    width: 1200px; height: 930px; overflow: hidden;
    background: var(--backdrop);
  }
  .stage { position: relative; width: 1200px; height: 930px; }
  .card {
    position: absolute;
    width: 620px; height: 354px;
    border-radius: 18px;
    background: linear-gradient(135deg, var(--card-edge), var(--card) 60%);
    overflow: hidden;
    box-shadow: 0 18px 40px rgba(0,0,0,.45);
  }
  .card--front { left: 80px; top: 90px; }
  .card--back  { left: 500px; top: 486px; }

  .forest-band {
    position: absolute; left: 0; right: 0; bottom: 0; height: 130px;
    background: linear-gradient(to top, var(--forest), rgba(58,52,36,0));
  }

  .brand {
    position: absolute;
    display: flex; align-items: center; gap: 14px;
  }
  .brand__dot {
    border-radius: 50%; background: var(--gold); flex: none;
  }
  .brand__text { display: flex; flex-direction: column; }
  .brand__name {
    font-family: "Cinzel", serif; font-weight: 600;
    color: var(--white); letter-spacing: 1px; line-height: 1.1;
    text-transform: uppercase;
  }
  .brand__tagline {
    font-family: "Cinzel", serif; font-weight: 400;
    color: var(--gold); text-transform: uppercase;
    margin-top: 6px;
  }

  .card--front .brand { left: 0; right: 0; top: 122px; justify-content: center; }
  .card--front .brand__dot { width: 34px; height: 34px; }
  .card--front .brand__name { font-size: 34px; }
  .card--front .brand__tagline { font-size: 17px; letter-spacing: 8px; }

  .card--back .brand { left: 38px; top: 140px; }
  .card--back .brand__dot { width: 26px; height: 26px; }
  .card--back .brand__name { font-size: 22px; width: 180px; }
  .card--back .brand__tagline { font-size: 11px; letter-spacing: 4px; }

  .divider {
    position: absolute; left: 268px; top: 70px;
    width: 2px; height: 200px; background: var(--gold);
  }
  .contact {
    position: absolute; left: 296px; top: 78px;
    font-family: "Roboto", sans-serif; color: var(--white);
  }
  .contact__names {
    font-weight: 500; font-size: 22px; color: var(--gold);
    text-transform: uppercase; letter-spacing: .3px;
  }
  .contact__surname { font-size: 15px; margin: 2px 0 0 14px; }
  .contact__list { list-style: none; margin-top: 26px; }
  .contact__item {
    display: flex; align-items: center; gap: 9px;
    font-size: 15px; margin-bottom: 8px;
  }
  .contact__item svg { width: 12px; height: 12px; flex: none; }
</style>
</head>
<body>
<main class="stage">

  <section class="card card--front" aria-label="Card front">
    <div class="forest-band" role="img" aria-label="Faint pine forest silhouette"></div>
    <div class="brand">
      <span class="brand__dot"></span>
      <div class="brand__text">
        <span class="brand__name">Cedar Hollow Scales</span>
        <span class="brand__tagline">Reptile Breeder</span>
      </div>
    </div>
  </section>

  <section class="card card--back" aria-label="Card back">
    <div class="forest-band" role="img" aria-label="Faint pine forest silhouette"></div>
    <div class="brand">
      <span class="brand__dot"></span>
      <div class="brand__text">
        <span class="brand__name">Cedar Hollow Scales</span>
        <span class="brand__tagline">Reptile Breeder</span>
      </div>
    </div>
    <div class="divider"></div>
    <div class="contact">
      <p class="contact__names">Grant and Melinda</p>
      <p class="contact__surname">Barlow</p>
      <ul class="contact__list">
        <li class="contact__item">
          <svg viewBox="0 0 12 12"><path d="M6 0a4 4 0 0 0-4 4c0 3 4 8 4 8s4-5 4-8a4 4 0 0 0-4-4zm0 5.5A1.5 1.5 0 1 1 6 2.5a1.5 1.5 0 0 1 0 3z" fill="var(--gold)"/></svg>
          Briar Bend, TX.
        </li>
        <li class="contact__item">
          <svg viewBox="0 0 12 12"><rect x="1" y="1" width="10" height="10" rx="2.5" fill="none" stroke="var(--gold)" stroke-width="1.6"/></svg>
          cedarhollowscales
        </li>
        <li class="contact__item">
          <svg viewBox="0 0 12 12"><rect x="0.8" y="2" width="10.4" height="8" fill="none" stroke="var(--gold)" stroke-width="1.2"/><path d="M1 2.5 6 6.5 11 2.5" fill="none" stroke="var(--gold)" stroke-width="1.2"/></svg>
          cedarhollowscales@mailhub.example
        </li>
      </ul>
    </div>
  </section>

</main>
</body>
</html>
```